Catchy Cards for Hospital

I run a rural hospital in Texas called Pelham Ridge Hospital and am in need of contemporary business cards for all of my Department Heads. While our logo is somewhat simplistic, I don't have the option of changing it at this time, so anything to make the rest of the card present the appearance of a modern, professional healthcare facility would be great. Although the attached files are in black, our hospital colors are in a copper brown and black. I need to be able to change the name and title on the card so I can get cards printed for various department heads.

Target Market(s)

Referring physicians, large hospital systems, national organizations, state and federal government

Industry/Entity Type

Hospital

Contact Information for Business Card

Name Derek Solano
Title CEO

Phone: Main 325-740-2386 & Direct xxxxxx
Fax xxxxx
derek.solano@pelhamrh.com
382 Wilmot Street Box 415
Harlow Springs 76291

Font styles to use
Serif

Colors
f48340

Requirements
Must have
• Clean crisp lines and ability to modify names, titles and emails
• On the back "PelhamRidgeHospital.Com
Nice to have
• Needs to be in line with logo, which is a bit dated and not too appealing, but I'm hoping that the rest of the card can make up for that fact just a little bit.
• Hospital's colors are a copper brown, black and white
Should not have
• Shapes or anything distracting

```html
<!DOCTYPE html>
<html lang="en">
<head>
<meta charset="utf-8">
<title>Pelham Ridge Hospital – Business Card</title>
<link rel="stylesheet" href="https://fonts.googleapis.com/css2?family=Tinos:wght@400;700&family=Cinzel:wght@400&display=swap">
<style>
  :root {
    --backdrop: #d9d9d9;
    --card: #000000;
    --copper: #f48340;
    --ink-light: #ffffff;
  }
  * { margin: 0; padding: 0; box-sizing: border-box; }
  html, body { width: 900px; height: 1200px; overflow: hidden; }
  body { background: var(--backdrop); position: relative; font-family: "Tinos", "Times New Roman", serif; }

  .card {
    position: absolute;
    left: 161px;
    width: 586px;
    height: 342px;
    background: var(--card);
  }
  .card--front { top: 221px; }
  .card--back { top: 636px; }

  .wordmark {
    position: absolute;
    font-family: "Tinos", "Times New Roman", serif;
    font-weight: 700;
    color: var(--copper);
    line-height: 1.02;
  }
  .card--front .wordmark { left: 46px; top: 112px; font-size: 40px; }
  .card--back .wordmark { left: 0; width: 586px; top: 96px; font-size: 42px; text-align: center; }

  .identity {
    position: absolute;
    right: 44px;
    top: 44px;
    text-align: right;
  }
  .identity__name { color: var(--ink-light); font-weight: 700; font-size: 17px; letter-spacing: 0.5px; }
  .identity__title { color: var(--copper); font-size: 14px; margin-top: 2px; }
  .identity__address { color: var(--ink-light); font-size: 13px; line-height: 19px; margin-top: 6px; }

  .contact-list {
    position: absolute;
    right: 44px;
    top: 215px;
    list-style: none;
  }
  .contact-list__item {
    display: flex;
    justify-content: flex-end;
    align-items: center;
    gap: 9px;
    height: 20.5px;
    color: var(--ink-light);
    font-size: 13px;
  }
  .contact-list__icon { width: 15px; height: 14px; display: block; }

  .website {
    position: absolute;
    left: 0;
    width: 586px;
    bottom: 32px;
    text-align: center;
    font-family: "Cinzel", "Times New Roman", serif;
    font-size: 14px;
    color: var(--copper);
    letter-spacing: 0.3px;
  }
</style>
</head>
<body>

<section class="card card--front">
  <div class="wordmark">Pelham Ridge<br>Hospital</div>

  <div class="identity">
    <div class="identity__name">DEREK SOLANO</div>
    <div class="identity__title">CEO</div>
    <div class="identity__address">382 Wilmot Street Box 415<br>Harlow Springs 76291</div>
  </div>

  <ul class="contact-list">
    <li class="contact-list__item">325-740-2386
      <svg class="contact-list__icon" viewBox="0 0 15 14" aria-label="Phone"><rect width="15" height="14" rx="2" fill="#f48340"/><path d="M3 6c0-2 2-3 4.5-3S12 4 12 6h-2.2V5H5.2v1z M4.5 7h6l1 4h-8z" fill="#000"/></svg>
    </li>
    <li class="contact-list__item">432-615-0948
      <svg class="contact-list__icon" viewBox="0 0 15 14" aria-label="Direct phone"><rect width="15" height="14" rx="2" fill="#f48340"/><path d="M3 6c0-2 2-3 4.5-3S12 4 12 6h-2.2V5H5.2v1z M4.5 7h6l1 4h-8z" fill="#000"/></svg>
    </li>
    <li class="contact-list__item">432-615-0948
      <svg class="contact-list__icon" viewBox="0 0 15 14" aria-label="Fax"><rect width="15" height="14" rx="2" fill="#f48340"/><path d="M5 2.5h5v3H5z M3 6h9v5H3z" fill="#000"/><rect x="5" y="8.5" width="5" height="1" fill="#f48340"/></svg>
    </li>
    <li class="contact-list__item">derek.solano@pelhamrh.com
      <svg class="contact-list__icon" viewBox="0 0 15 14" aria-label="Email"><rect width="15" height="14" rx="2" fill="#f48340"/><rect x="3" y="4" width="9" height="6" fill="#000"/><path d="M3 4l4.5 3.5L12 4" stroke="#f48340" stroke-width="1" fill="none"/></svg>
    </li>
  </ul>
</section>

<section class="card card--back">
  <div class="wordmark">Pelham Ridge<br>Hospital</div>
  <div class="website">WWW.PELHAMRIDGEHOSPITAL.COM</div>
</section>

</body>
</html>
```